The Bright Harbor Hour (By Line: Making an Impact through Effective Leadership)

I am seeking the design and creation of a”banner ad image” for my radio program entitled “The Bright Harbor Hour.” The banner created should capture the look and feel of an image that reflects the vision statement below and that fosters the intent reflected by the principal goals listed below:

Vision statement

The Bright Harbor Hour is a powerfully engaging platform for great conversations about leadership and leadership learning.

Goals

1. Build a community of listeners who will be made to feel invited and excited about being connected to the show, it host and its broader community of listeners.

2. Provide interesting, intelligent and meaningful conversations about leadership and learning by the host, invited guests, both in studio and online.
The banner should be one that speaks to/invites listeners to become members of a community of listeners seeking to listen to and learn about the subject of leadership and leadership improvement.

The acceptable (final) banner should be professional in image, style and substance. The Photo shop layered file is required so that the banner image can be altered and adapted for use in PDF or text documents.

Finally, it is a banner that I intend to repopulate across several medium’s, such as kwelto, pine dock, etc. as a part of the process of establishing an image – brand – for the radio show as reflected the vision statement and goals.

While the target audience described is broad, it is anticipated that the primary listeners will be those who are leaders and serving in such roles as CEO’s, Vice Presidents, and other leaders in business, government and other local organizational capacities including students interested in learning about and discussing the subject of leadership.

Target Market(s)

Those who are interested in the topic of leadership and are actively engaged in leading as supervisors, managers and executives. These would be CEO, VP, and other C-level leaders in business, private and public sector organizations. It is also anticipated that those who are students of leadership learning will find my program a great resource.

Industry/Entity Type

Radio

Colors
3176b5
b768aa
d3a5cc

Requirements
Must have
• Be unique, attractive and capture the look and feel as noted in the description of the project.
Nice to have
• Note: I will have a head shot photo included in the banner so a place holder needs to be included for that

```html
<!DOCTYPE html>
<html lang="en">
<head>
<meta charset="utf-8">
<title>The Bright Harbor Hour – Banner Designs</title>
<link href="https://fonts.googleapis.com/css2?family=Oswald:wght@400;500;600&family=Montserrat:wght@700;800&family=Great+Vibes&family=Josefin+Sans:wght@400&display=swap" rel="stylesheet">
<style>
  :root {
    --page-bg: #eef0f2;
    --blue: #3176b5;
    --blue-light: #4aa3dc;
    --blue-deep: #1f5f9c;
    --purple: #b768aa;
    --lilac: #d3a5cc;
    --white: #ffffff;
    --ink: #2b2b2b;
    --grey-bg: #ededed;
    --teal: #1fa3b8;
    --salmon: #ef7b6f;
    --live-red: #e02d2d;
    --photo-suit: #3b4048;
    --photo-light: #d9d9d9;
  }
  * { box-sizing: border-box; margin: 0; padding: 0; }
  html, body { width: 835px; height: 1200px; overflow: hidden; }
  body { background: var(--page-bg); position: relative; font-family: "Montserrat", sans-serif; }

  .banner { position: absolute; left: 87px; width: 661px; height: 251px; overflow: hidden; }
  .banner-one { top: 97px; background: linear-gradient(135deg, var(--blue-light) 0%, var(--blue) 60%, var(--blue-deep) 100%); }
  .banner-two { top: 452px; background: radial-gradient(ellipse at 50% 50%, #ffffff 0%, var(--grey-bg) 75%); }
  .banner-three { top: 807px; background: var(--white); }

  .design-label {
    position: absolute; left: 0; width: 835px; text-align: center;
    font-family: "Josefin Sans", sans-serif; font-size: 22px; letter-spacing: 3px; color: var(--ink);
  }
  .label-one { top: 366px; }
  .label-two { top: 721px; }
  .label-three { top: 1077px; }

  .photo { position: absolute; }

  /* Design 1 */
  .headshot-one { left: 0; top: 0; width: 240px; height: 251px;
    background: linear-gradient(180deg, rgba(255,255,255,0) 0%, rgba(255,255,255,0) 40%, var(--photo-suit) 75%); }
  .mic-one { left: 492px; top: 14px; width: 80px; height: 185px;
    background: linear-gradient(180deg, #c83a3a 0%, #c83a3a 22%, #cfd3d8 23%, #8e949b 70%, #2e3135 100%); border-radius: 36px 36px 12px 12px; }
  .one-the { position: absolute; left: 240px; top: 30px; font-family: "Great Vibes", cursive; font-size: 46px; color: var(--white); line-height: 1; }
  .one-title { position: absolute; left: 258px; top: 66px; font-family: "Oswald", sans-serif; font-weight: 500; color: var(--white); line-height: 1; text-transform: uppercase; white-space: nowrap; }
  .one-title .line-a { display: block; font-size: 33px; }
  .one-title .line-b { display: block; font-size: 84px; margin-top: 2px; }
  .one-bar { position: absolute; left: 240px; top: 208px; width: 421px; height: 30px; background: var(--purple);
    font-family: "Oswald", sans-serif; font-size: 16px; color: var(--white); line-height: 30px; padding-left: 18px; letter-spacing: 0.3px; white-space: nowrap; }

  /* Design 2 */
  .wave-two { left: 0; top: 105px; width: 661px; height: 60px;
    background: linear-gradient(180deg, rgba(200,200,200,0) 0%, rgba(200,200,200,0.55) 50%, rgba(200,200,200,0) 100%); }
  .mic-two { left: 45px; top: 112px; width: 72px; height: 139px;
    background: linear-gradient(180deg, #e8e8e8 0%, #9a9a9a 55%, #5c5c5c 100%); border-radius: 36px 36px 10px 10px; }
  .headshot-two { left: 432px; top: 0; width: 220px; height: 251px;
    background: linear-gradient(180deg, rgba(255,255,255,0) 0%, rgba(255,255,255,0) 35%, #c9cbcf 60%, #b5b8bd 100%); }
  .two-copy { position: absolute; left: 38px; top: 30px; color: var(--blue); font-weight: 800; text-transform: uppercase; line-height: 1; white-space: nowrap; }
  .two-copy .the { display: block; font-size: 21px; margin-left: 8px; }
  .two-copy .line-a { display: block; font-size: 39px; margin-top: 9px; letter-spacing: -1px; }
  .two-copy .line-b { display: block; font-size: 39px; margin-top: 14px; margin-left: 140px; letter-spacing: -1px; }
  .two-host { position: absolute; left: 152px; top: 166px; font-weight: 800; font-size: 17px; line-height: 1; color: var(--purple); text-transform: uppercase; white-space: nowrap; }
  .two-bar { position: absolute; left: 108px; top: 190px; width: 270px; height: 26px; background: var(--purple);
    font-weight: 700; font-size: 13px; color: var(--white); line-height: 26px; text-align: center; white-space: nowrap; }

  /* Design 3 */
  .headshot-three { left: 0; top: 0; width: 225px; height: 251px;
    background: linear-gradient(180deg, var(--photo-light) 0%, #bfc3c7 50%, #c5c7ca 100%); }
  .three-shapes { position: absolute; left: 0; top: 0; }
  .three-save { position: absolute; left: 232px; top: 4px; width: 110px; text-align: center; color: var(--white);
    font-weight: 800; font-size: 21px; line-height: 0.95; text-transform: uppercase; }
  .three-when { position: absolute; left: 360px; top: 12px; width: 290px; text-align: center; color: var(--white); font-weight: 700; }
  .three-when .day { display: block; font-size: 27px; text-transform: uppercase; }
  .three-when .time { display: block; font-size: 16px; margin-top: 2px; }
  .three-title { position: absolute; left: 232px; top: 118px; width: 420px; text-align: center; color: var(--white);
    font-weight: 700; text-transform: uppercase; line-height: 1.02; }
  .three-title .line-a { display: block; font-size: 30px; }
  .three-title .line-b { display: block; font-size: 36px; }
  .three-byline { position: absolute; left: 285px; top: 208px; color: var(--white); font-weight: 700; font-size: 13px; text-transform: uppercase; display: flex; align-items: center; gap: 8px; }
  .live-tag { background: var(--live-red); padding: 2px 7px; font-size: 13px; }
</style>
</head>
<body>

  <section class="banner banner-one">
    <div class="photo headshot-one" role="img" aria-label="Host headshot placeholder: smiling man in dark suit and tie"></div>
    <div class="photo mic-one" role="img" aria-label="Studio microphone with on-air sign"></div>
    <span class="one-the">The</span>
    <h1 class="one-title"><span class="line-a">Bright Harbor</span><span class="line-b">Hour</span></h1>
    <div class="one-bar">FROM EVERY MON TO SAT AT 9:00 AM TO 12:00 AM</div>
  </section>
  <p class="design-label label-one">DESIGN #1</p>

  <section class="banner banner-two">
    <div class="photo wave-two" role="img" aria-label="Faint audio sound wave band"></div>
    <div class="photo mic-two" role="img" aria-label="Vintage chrome microphone"></div>
    <h1 class="two-copy"><span class="the">The</span><span class="line-a">Bright Harbor</span><span class="line-b">Hour</span></h1>
    <p class="two-host">Starring Alex Marlow</p>
    <div class="two-bar">MON - SAT AT 9:00AM - 11:00AM</div>
    <div class="photo headshot-two" role="img" aria-label="Host headshot placeholder: man in light grey suit with arms crossed"></div>
  </section>
  <p class="design-label label-two">DESIGN #2</p>

  <section class="banner banner-three">
    <div class="photo headshot-three" role="img" aria-label="Host headshot placeholder: smiling man in grey suit, blurred office behind"></div>
    <svg class="three-shapes" width="661" height="251" viewBox="0 0 661 251" aria-hidden="true">
      <polygon points="225,0 345,0 345,30 358,40 345,50 345,84 225,84" fill="var(--purple)"/>
      <polygon points="352,0 661,0 661,78 405,78 390,96 388,78 352,78" fill="var(--salmon)"/>
      <polygon points="225,84 661,84 661,251 225,251 225,180 212,168 225,156" fill="var(--teal)"/>
      <rect x="345" y="0" width="7" height="84" fill="var(--white)"/>
      <rect x="225" y="78" width="436" height="6" fill="var(--white)"/>
    </svg>
    <p class="three-save">Save<br>the<br>date</p>
    <p class="three-when"><span class="day">On Friday</span><span class="time">9:00AM TO 11:00AM</span></p>
    <h1 class="three-title"><span class="line-a">The Bright Harbor</span><span class="line-b">Hour 2017</span></h1>
    <p class="three-byline"><span class="live-tag">LIVE</span><span>By Mr. Alex Marlow</span></p>
  </section>
  <p class="design-label label-three">DESIGN #3</p>

</body>
</html>
```